Colon Cancer Fundraiser Fall 2015

We need a flier design for a fundraiser in September. The event is in our hometown. It is an informal dinner, silent auction, and live band. Family Friendly.

www.brightpathwaynfp.org

Marlow Veterans Hall
September 26 3pm - 10pm
Bean Bag Tournament @ 4pm
Band @ 7 Band Name: Velvet Orchard

Industry/Entity Type

Event

Font styles to use
Sans Serif

Requirements
Must have
• www.brightpathwaynfp.org
• Marlow Veterans Hall
• September 26 3pm - 10pm
• Bean Bag Tournament @ 4pm
• Band @ 7 Band Name: Velvet Orchard
• Contact: Brenda 708-555-0193 brenda@brightpathwaynfp.org

```html
<!DOCTYPE html>
<html lang="en">
<head>
<meta charset="utf-8">
<title>Colon Cancer Fundraiser Fall 2015</title>
<link rel="stylesheet" href="https://fonts.googleapis.com/css2?family=Oswald:wght@300;400;500&display=swap">
<style>
  :root {
    --paper: #f8f5ef;
    --paper-edge: #efe9df;
    --band: #fbfaf7;
    --ink: #4a4744;
    --ink-soft: #6b6763;
    --autumn: #e8864a;
    --autumn-deep: #d9692f;
    --leaf-gold: #f0b36a;
    --leaf-rust: #d77a3c;
    --rule: #b9b3ab;
  }
  * { margin: 0; padding: 0; box-sizing: border-box; }
  html, body {
    width: 900px;
    height: 1200px;
    overflow: hidden;
  }
  body {
    font-family: "Oswald", "Arial Narrow", sans-serif;
    background: var(--paper);
  }
  .flyer {
    position: relative;
    width: 900px;
    height: 1200px;
    overflow: hidden;
    background: radial-gradient(ellipse at 50% 45%, var(--paper) 55%, var(--paper-edge) 100%);
  }
  .leaves {
    position: absolute;
    border-radius: 50%;
    opacity: 0.8;
  }
  .leaves--top {
    top: -170px;
    right: -150px;
    width: 620px;
    height: 560px;
    background: radial-gradient(circle at 55% 50%, var(--leaf-rust) 0%, var(--leaf-gold) 36%, rgba(240,179,106,0.35) 56%, rgba(248,245,239,0) 70%);
  }
  .leaves--bottom {
    bottom: -120px;
    left: -170px;
    width: 560px;
    height: 620px;
    background: radial-gradient(circle at 50% 50%, var(--leaf-rust) 0%, var(--leaf-gold) 32%, rgba(240,179,106,0.3) 54%, rgba(248,245,239,0) 70%);
  }
  .title-band {
    position: absolute;
    top: 318px;
    left: 0;
    width: 100%;
    height: 108px;
    background: rgba(251,250,247,0.85);
    border-top: 2px solid var(--rule);
    border-bottom: 2px solid var(--rule);
    box-shadow: 0 6px 10px rgba(0,0,0,0.06);
    display: flex;
    align-items: center;
    justify-content: center;
  }
  .event-title {
    font-weight: 400;
    font-size: 46px;
    letter-spacing: 1.5px;
    color: var(--ink);
    text-transform: uppercase;
  }
  .event-date {
    position: absolute;
    top: 484px;
    width: 100%;
    text-align: center;
    font-weight: 300;
    font-size: 32px;
    letter-spacing: 1px;
    color: var(--autumn);
    text-transform: uppercase;
  }
  .event-date strong { font-weight: 500; color: var(--autumn-deep); }
  .event-features {
    position: absolute;
    top: 600px;
    width: 100%;
    list-style: none;
    text-align: center;
    font-weight: 300;
    font-size: 23px;
    line-height: 38px;
    color: var(--autumn);
  }
  .schedule {
    position: absolute;
    top: 866px;
    left: 250px;
    right: 170px;
    border-top: 2px solid var(--rule);
    border-bottom: 2px solid var(--rule);
    padding: 16px 0 18px;
    text-align: center;
  }
  .schedule__tournament {
    font-weight: 300;
    font-size: 36px;
    letter-spacing: 1px;
    color: var(--ink);
    text-transform: uppercase;
  }
  .schedule__band {
    margin-top: 8px;
    font-weight: 300;
    font-size: 22px;
    color: var(--ink-soft);
  }
  .schedule__band-name {
    margin-left: 8px;
    text-transform: uppercase;
    letter-spacing: 1px;
    font-weight: 400;
    color: var(--ink);
  }
  .event-details {
    position: absolute;
    top: 1050px;
    left: 250px;
    right: 170px;
    text-align: center;
    font-weight: 300;
    font-size: 20px;
    line-height: 32px;
    color: var(--ink-soft);
  }
  .event-details__venue {
    font-weight: 400;
    font-size: 22px;
    letter-spacing: 1px;
    text-transform: uppercase;
    color: var(--autumn-deep);
  }
  .event-details__web {
    color: var(--ink);
    font-weight: 400;
  }
</style>
</head>
<body>
  <main class="flyer">
    <div class="leaves leaves--top" role="img" aria-label="Watercolour autumn maple leaves in orange and gold"></div>
    <div class="leaves leaves--bottom" role="img" aria-label="Watercolour autumn maple leaves in orange and gold"></div>

    <header class="title-band">
      <h1 class="event-title">Colon Cancer Fundraiser Fall 2015</h1>
    </header>

    <p class="event-date">September <strong>26st</strong> from <strong>3pm - 10pm</strong></p>

    <ul class="event-features">
      <li>Informal Dinner</li>
      <li>Silent Auction</li>
      <li>&amp; Live Band</li>
    </ul>

    <section class="schedule">
      <p class="schedule__tournament">Bean Bag Tournament at 4pm</p>
      <p class="schedule__band">Band at 7 pm<span class="schedule__band-name">Velvet Orchard</span></p>
    </section>

    <footer class="event-details">
      <p class="event-details__venue">Marlow Veterans Hall</p>
      <p>Contact: Brenda &middot; 708-555-0193 &middot; brenda@brightpathwaynfp.org</p>
      <p class="event-details__web">www.brightpathwaynfp.org</p>
    </footer>
  </main>
</body>
</html>
```